Broschüre für Bauingenieurbüro
Zielgruppe
Wir sind ein kleines Bauingenieurbüro mit bis 10 Mitarbeiterinnen. Wir wollen uns bei bestehenden Kunden mit der Broschüre in Erinnerung rufen und für neue Kunden genügend Informationen und Schlagkraft aufzeigen, dass diese uns Aufträge zukommen lassen. Zu unseren Kunden gehören hauptsächlich Architekturbüros und wenige Privatpersonen als Bauherren.
Aufgabenstellung
Wir möchten die Broschüre auf A3 doppelseitig mit einem Falz in der Mitte haben (Zusammengefaltet soll die Broschüre das Format A4 aufweisen). Unser bestehendes Porträt wird dem Auftrag beigelegt (PDF Rohversion Seite 3 und 4). Das Dokument 'Veränderung Firmenporträt 220818' zeigt unsere Wünsche auf. Das Design der Broschüre soll dann in einem weiteren Schritt auch auf die Homepage übergehen.

```html
<!DOCTYPE html>
<html lang="de">
<head>
<meta charset="utf-8">
<title>kelder ingenieure – Kurzportrait 2022</title>
<link href="https://fonts.googleapis.com/css2?family=Montserrat:wght@400;500;600;700;800&display=swap" rel="stylesheet">
<style>
:root{
  --bg:#adb6be;
  --ink:#2a2a2a;
  --dark:#262626;
  --dark-cell:#2e2e2e;
  --grey-cell:#9b9b9b;
  --gold:#a8864f;
  --beige:#cdbf9e;
  --beige-light:#ddd3bc;
  --paper:#ffffff;
  --paper-grey:#f0f0f0;
  --muted:#6b6b6b;
  --rule:#c9c9c9;
}
*{box-sizing:border-box;margin:0;padding:0}
html,body{width:1200px;height:3008px;overflow:hidden}
body{background:var(--bg);font-family:"Montserrat",sans-serif;color:var(--ink);position:relative}
.spread{position:absolute;left:50px;width:1100px;height:776px;display:flex;box-shadow:0 10px 30px rgba(0,0,0,.18)}
.spread--cover{top:500px}
.spread--inner{top:1730px}
.page{position:relative;width:550px;height:776px;overflow:hidden}
.abs{position:absolute}

/* brand */
.brand{display:flex;align-items:center;gap:6px;font-weight:500;line-height:1}
.brand__name{display:flex;flex-direction:column;font-size:14px;letter-spacing:.3px}
.brand__name span:last-child{font-size:9px;letter-spacing:.6px;margin-top:2px}
.brand__mark{width:12px;height:12px;background:currentColor}
.brand--light{color:#e8e8e8}
.brand--dark{color:#3a3a3a}
.brand--large .brand__name{font-size:30px}
.brand--large .brand__name span:last-child{font-size:18px;margin-top:4px}
.brand--large .brand__mark{width:24px;height:24px}

.head-rule{position:absolute;height:1px;background:#5a5a5a}
.head-rule--light{background:var(--rule)}
.title{font-weight:700;font-size:28px;color:var(--gold);letter-spacing:.3px}
.title-bar{width:34px;height:2px;background:var(--beige)}
.footer{font-size:6.5px;color:var(--muted)}

/* references */
.refs{left:42px;top:189px;display:grid;grid-template-columns:repeat(3,146px);column-gap:16px;row-gap:19px}
.ref{background:#fff;height:141px;padding:5px}
.ref__photo{height:97px;background:linear-gradient(160deg,#7b8a6a,#9b7a55 55%,#5f6b52)}
.ref__photo--2{background:linear-gradient(170deg,#b8c0c8,#a59579 50%,#6d6a5c)}
.ref__photo--3{background:linear-gradient(165deg,#8e9aa4,#b09a7c 55%,#6f6a60)}
.ref__photo--4{background:linear-gradient(180deg,#aab7c4,#8c8c86 55%,#5d6b4c)}
.ref__photo--5{background:linear-gradient(160deg,#6e7466,#9a8468 55%,#4f5448)}
.ref__photo--6{background:linear-gradient(165deg,#5d6456,#a06a44 55%,#4e4a40)}
.ref__cap{text-align:center;font-size:6.5px;line-height:1.3;margin-top:6px;color:#222}
.ref__cap b{font-weight:700;display:block}
.label{font-size:9px;font-weight:700;color:var(--beige)}
.small-bar{width:16px;height:1px;background:var(--beige);margin-top:5px}
.note{font-size:9px;color:#e6e6e6}

.contact-band{left:0;top:605px;width:550px;height:171px;background:var(--beige)}
.contact{font-size:9px;line-height:1.3;color:#3a3a3a}
.contact-row{display:flex;align-items:center;gap:10px;font-size:9px;color:#3a3a3a}
.contact-row svg{width:12px;height:12px}

/* cover */
.cover{background:linear-gradient(180deg,#fafafa,#f4f4f4)}
.url{font-size:6.5px;font-weight:600;color:#444}
.hero{left:0;top:144px;width:550px;height:400px;background:radial-gradient(ellipse at 55% 55%,#d9dde3 0%,#c89a78 28%,#b9b9b6 45%,#f4f4f4 75%)}
.cover-title{font-size:34px;font-weight:700;color:var(--gold);letter-spacing:1px}
.cover-sub{font-size:11.5px;font-weight:600;color:#333}
.gold-line{height:1px;background:var(--gold)}
.year{font-size:96px;font-weight:600;color:transparent;-webkit-text-stroke:1px #d8d8d8;letter-spacing:2px;line-height:1}

/* inner */
.inner-left{background:var(--paper)}
.inner-right{background:var(--paper-grey)}
.faint-drawing{background:radial-gradient(ellipse at 50% 70%,rgba(200,170,140,.25),rgba(220,220,220,.2) 45%,rgba(255,255,255,0) 75%)}
.body{font-size:9px;line-height:1.35;color:#333}
.body p+p{margin-top:11px}
.strong{font-size:9px;font-weight:700;color:#333}
.matrix{left:40px;top:321px;width:379px;display:grid;grid-template-columns:1fr 1fr}
.cell{height:78px;display:flex;align-items:center;font-size:8.5px;line-height:1.3}
.cell--left{padding-left:23px;color:#eee;clip-path:polygon(0 0,92% 0,100% 50%,92% 100%,0 100%);position:relative;z-index:1;margin-right:-14px}
.cell--right{padding-left:37px;color:#3a3a3a}
.cell--dark{background:var(--dark-cell)}
.cell--grey{background:var(--grey-cell)}
.cell--beige{background:var(--beige)}
.cell--beige-light{background:var(--beige-light)}
.row-even .cell--left{color:#f2f2f2}

.subtitle{font-size:9.5px;font-weight:600;color:#333;line-height:1.4}
.skill{position:absolute;left:50px;width:470px;display:flex;gap:17px}
.skill__icon{width:20px;height:20px;flex:none;color:#777}
.skill__title{font-size:9px;font-weight:700;color:#222}
.skill__text{font-size:8px;line-height:1.4;color:#444;margin-top:1px}
.section-label{font-size:9.5px;font-weight:700;color:var(--gold);line-height:1.4}
.section-label span{color:#333;font-weight:600}
</style>
</head>
<body>

<!-- Outer spread: references + cover -->
<section class="spread spread--cover">
  <div class="page" style="background:var(--dark)">
    <div class="abs brand brand--light" style="left:42px;top:30px">
      <div class="brand__name"><span>kelder</span><span>ingenieure</span></div>
      <span class="brand__mark"></span>
    </div>
    <div class="head-rule" style="left:142px;top:42px;width:370px"></div>

    <h2 class="abs title" style="left:42px;top:100px">Referenzen</h2>
    <div class="abs title-bar" style="left:42px;top:151px"></div>

    <div class="abs refs">
      <figure class="ref"><div class="ref__photo" role="img" aria-label="Luftaufnahme Baustelle Mehrfamilienhaus"></div><figcaption class="ref__cap"><b>Neubau MFH Lindenweg 1</b>8234 Talwil</figcaption></figure>
      <figure class="ref"><div class="ref__photo ref__photo--2" role="img" aria-label="Luftaufnahme Umbau Pflegeheim"></div><figcaption class="ref__cap"><b>Neu- und Umbau Pflegeheim für Menschen mit Demenz</b>8207 Rheinau-Ost</figcaption></figure>
      <figure class="ref"><div class="ref__photo ref__photo--3" role="img" aria-label="Luftaufnahme Baugrube Neubau"></div><figcaption class="ref__cap"><b>Neubau MFH Mühlenbach</b>8215 Hofacker</figcaption></figure>
      <figure class="ref"><div class="ref__photo ref__photo--4" role="img" aria-label="Luftaufnahme Schloss mit Anbau"></div><figcaption class="ref__cap"><b>Um- &amp; Anbau Schloss Eichenau</b>8536 Seewil</figcaption></figure>
      <figure class="ref"><div class="ref__photo ref__photo--5" role="img" aria-label="Luftaufnahme Neubau Restaurant"></div><figcaption class="ref__cap"><b>Neubau Restaurant Kalkofen</b>8200 Rheinau-Ost</figcaption></figure>
      <figure class="ref"><div class="ref__photo ref__photo--6" role="img" aria-label="Luftaufnahme Rohbau drei Mehrfamilienhäuser"></div><figcaption class="ref__cap"><b>Neubau 3 MFH Weitblick</b>8234 Talwil</figcaption></figure>
    </div>

    <div class="abs" style="left:42px;top:512px"><div class="label">Standort</div><div class="small-bar"></div></div>
    <p class="abs note" style="left:42px;top:542px">Weitere Referenzen finden Sie auf unserer Homepage www.kelder-ing.ch</p>

    <div class="abs contact-band"></div>
    <address class="abs contact" style="left:42px;top:634px;font-style:normal">1456 Street Name, Suite 18<br>Zip City 90210<br>Country</address>
    <div class="abs contact-row" style="left:42px;top:684px">
      <svg viewBox="0 0 24 24" fill="none" stroke="#3a3a3a" stroke-width="1.6"><path d="M5 3h4l2 5-2.5 1.5a11 11 0 0 0 6 6L16 13l5 2v4a2 2 0 0 1-2 2A16 16 0 0 1 3 5a2 2 0 0 1 2-2z"/></svg>555 0142 1251</div>
    <div class="abs contact-row" style="left:42px;top:702px">
      <svg viewBox="0 0 24 24" fill="none" stroke="#3a3a3a" stroke-width="1.6"><rect x="3" y="5" width="18" height="14"/><path d="M3 6l9 7 9-7"/></svg>info@kelder-ing.ch</div>
    <p class="abs footer" style="left:42px;top:754px">Business Investment &nbsp;|&nbsp; 2022</p>
  </div>

  <div class="page cover">
    <p class="abs url" style="left:38px;top:36px">www.kelder-ing.ch</p>
    <div class="abs brand brand--dark brand--large" style="right:42px;top:40px">
      <div class="brand__name"><span>kelder</span><span>ingenieure</span></div>
      <span class="brand__mark"></span>
    </div>
    <div class="abs hero" role="img" aria-label="3D-Darstellung Mauerwerk, Betonwand und Bewehrung auf Bauplan"></div>
    <h1 class="abs cover-title" style="left:38px;top:600px">KURZPORTRAIT</h1>
    <p class="abs cover-sub" style="left:38px;top:647px">Mit uns findet Ihre Vision zur notwendigen Stabilität</p>
    <div class="abs gold-line" style="left:38px;top:738px;width:222px"></div>
    <div class="abs year" style="left:282px;top:676px">2022</div>
  </div>
</section>

<!-- Inner spread: profile + competences -->
<section class="spread spread--inner">
  <div class="page inner-left">
    <div class="abs faint-drawing" style="left:0;top:420px;width:550px;height:356px" role="img" aria-label="Blasse Hintergrunddarstellung Bewehrung und Bauplan"></div>
    <div class="abs brand brand--dark" style="left:42px;top:30px">
      <div class="brand__name"><span>kelder</span><span>ingenieure</span></div>
      <span class="brand__mark"></span>
    </div>
    <div class="head-rule head-rule--light" style="left:142px;top:42px;width:370px"></div>

    <h2 class="abs title" style="left:40px;top:100px">Wer wir sind</h2>
    <div class="abs title-bar" style="left:40px;top:151px"></div>

    <div class="abs body" style="left:40px;top:172px;width:400px">
      <p>Die kelder ingenieure gmbh ist ein unabhängiges, junges und dynamisches Bauingenieurbüro aus der Region Rheinau.</p>
      <p>Wir bieten sämtliche Bauingenieurleistungen im Hoch- und konstruktiven Ingenieurbau an.</p>
      <p>Wir planen und realisieren Neu- und Umbauten und führen bei älteren Gebäuden Tragwerkserhaltungen und -verstärkungen durch, womit die Nutzungsdauer erhöht oder eine Umnutzung ermöglicht wird.</p>
    </div>
    <p class="abs strong" style="left:40px;top:298px">Zu unseren gängigsten Bauobjekten gehören:</p>

    <div class="abs matrix">
      <div class="cell cell--left cell--dark">In der gesamten<br>Deutschschweiz in Ihrer<br>Nähe tätig</div>
      <div class="cell cell--right cell--beige">Projektbearbeitung nach<br>Wunsch in Deutsch<br>und Englisch</div>
      <div class="cell cell--left cell--grey">Fundiertes Fachwissen<br>und innovative<br>Lösungen</div>
      <div class="cell cell--right cell--beige-light">Engagiertes &amp; dynamisches<br>Team für tagtägliche<br>Höchstleistungen</div>
      <div class="cell cell--left cell--dark">Partnerschaftlicher<br>Umgang mit allen<br>Projektbeteiligten</div>
      <div class="cell cell--right cell--beige">Preiswerte<br>Dienstleistungen bei<br>höchster Arbeitsqualität</div>
      <div class="cell cell--left cell--grey">Täglich Einblicke in alle<br>Facetten des Hochbaus<br>schärfen uns den Blick aufs<br>Wesentliche</div>
      <div class="cell cell--right cell--beige-light">Schlanke, optimal auf Ihre<br>Bedürfnisse ausgerichtete<br>Prozesse</div>
      <div class="cell cell--left cell--dark">Laufende Aus- &amp;<br>Weiterbildung aller<br>Mitarbeiterinnen</div>
      <div class="cell cell--right cell--beige">Praxisnahes Planen auf dem<br>neuesten Stand der Technik –<br>in jeder Ingenieurdisziplin</div>
    </div>
    <p class="abs footer" style="left:40px;top:754px">Business Investment &nbsp;|&nbsp; 2022</p>
  </div>

  <div class="page inner-right">
    <div class="abs faint-drawing" style="left:0;top:360px;width:550px;height:416px" role="img" aria-label="Blasse Hintergrunddarstellung Mauerwerk und Bewehrung"></div>
    <div class="abs brand brand--dark" style="right:42px;top:30px">
      <div class="brand__name"><span>kelder</span><span>ingenieure</span></div>
      <span class="brand__mark"></span>
    </div>

    <h2 class="abs title" style="left:38px;top:100px">Kompetenzen</h2>
    <p class="abs subtitle" style="left:38px;top:143px">Klassischer Ingenieurhochbau<br>… unser Beitrag an Ihr Bauwerk</p>

    <div class="skill" style="top:223px">
      <svg class="skill__icon" viewBox="0 0 24 24" fill="none" stroke="currentColor" stroke-width="1.3"><path d="M12 3v17M6 20h12M4 7h16M4 7l-3 7h6zM20 7l-3 7h6z"/></svg>
      <div><div class="skill__title">Tragwerksplanung</div><div class="skill__text">Beton-, Stahl- &amp; Holzbau</div></div>
    </div>
    <div class="skill" style="top:272px;left:87px">
      <div><div class="skill__title">Tragwerkserhaltung | Tragwerksverstärkung</div><div class="skill__text">Zustandsuntersuchungen | Statische Nachweise | Erdbebensicherheit |<br>Verstärkungskonzepte</div></div>
    </div>
    <div class="skill" style="top:330px">
      <svg class="skill__icon" viewBox="0 0 24 24" fill="none" stroke="currentColor" stroke-width="1.3"><rect x="9" y="3" width="6" height="4"/><path d="M12 7v3M12 10l-6 11M12 10l6 11M12 10v11"/></svg>
      <div><div class="skill__title">Baugrube | Baugrubenüberwachung</div><div class="skill__text">Aushub | Baugrubensicherung | Wasserhaltung |<br>Überwachungskonzepte Baugrube &amp; Nachbarparzellen</div></div>
    </div>
    <div class="skill" style="top:386px">
      <svg class="skill__icon" viewBox="0 0 24 24" fill="none" stroke="currentColor" stroke-width="1.3"><path d="M5 4h12a2 2 0 0 1 2 2v14H7a2 2 0 0 1-2-2z M5 18a2 2 0 0 1 2-2h12"/></svg>
      <div><div class="skill__title">Leistungskatalog</div><div class="skill__text">Abbruch | Unter- &amp; Abfangungen | Schneiden &amp; Bohren | Sichern &amp; Ertüchtigen |<br>Kanalisationen | Wasserhaltung | Baugrubenabschlüsse | Pfahlfundationen |<br>Aushub | Beton-, Stahl- &amp; Holzbau | Mauerwerk</div></div>
    </div>
    <div class="skill" style="top:455px">
      <svg class="skill__icon" viewBox="0 0 24 24" fill="none" stroke="currentColor" stroke-width="1.3"><path d="M3 11l9-7 9 7M5 10v10h14V10M10 20v-6h4v6"/></svg>
      <div><div class="skill__title">Baupläne</div><div class="skill__text">Schalungs- &amp; Bewehrungspläne | Stahlbau- &amp; Holzbaupläne |<br>Aushubpläne inkl. Baugrubensicherung</div></div>
    </div>
    <div class="skill" style="top:507px">
      <svg class="skill__icon" viewBox="0 0 24 24" fill="none" stroke="currentColor" stroke-width="1.3"><path d="M4 20l2-6L17 3l4 4L10 18zM14 6l4 4"/></svg>
      <div><div class="skill__title">Digitalisierung | BIM</div><div class="skill__text">Tragwerksmodell inkl. allen statischen Einbauteilen | Mengenbestimmung ab Modell |<br>Kollisionsprüfung &amp; Qualitätssicherung am Modell</div></div>
    </div>
    <div class="skill" style="top:562px">
      <svg class="skill__icon" viewBox="0 0 24 24" fill="none" stroke="currentColor" stroke-width="1.3"><circle cx="5" cy="5" r="3"/><circle cx="19" cy="5" r="3"/><circle cx="5" cy="19" r="3"/><circle cx="19" cy="19" r="3"/><path d="M7 7l10 10M17 7L7 17"/><rect x="10" y="10" width="4" height="4"/></svg>
      <div><div class="skill__title">Drohnenflüge</div><div class="skill__text">Referenzfotos | Rissprotokolle Fassaden &amp; Strassen | Vermessung | Werbevideos</div></div>
    </div>

    <p class="abs section-label" style="left:38px;top:612px">Berufsbildung<br><span>… unser Beitrag an die Zukunft</span></p>
    <div class="skill" style="top:660px">
      <svg class="skill__icon" viewBox="0 0 24 24" fill="none" stroke="currentColor" stroke-width="1.3"><path d="M3 17h18M5 17a7 7 0 0 1 14 0M12 10V6M10 6h4"/></svg>
      <div><div class="skill__title">Lernende Zeichnerin Fachrichtung Ingenieurbau EFZ</div><div class="skill__text">Ausbildung Lernende</div></div>
    </div>
    <p class="abs footer" style="right:42px;top:754px">Business Investment &nbsp;|&nbsp; 2022</p>
  </div>
</section>

</body>
</html>
```